Logo + Business Card Design Project

We are looking at changing our logo and reprinting business cards.

Attached is a design concept for the logo (we have no hi res files for this).

The logo needs to be able to work standalone without the tagline.

We are happy for you to use this concept or design a new one. The existing concept is quite well liked.

We would also consider not having Solutions in the logo and just have QRV Systems Pty Ltd in the body text of the card.

We have a Tag Line that needs to go on all documentation / websites etc wherever the logo appears.

Tagline: Taking IT further

Our message to clients is that we have solutions that:

QRV Systems:
Taking IT further

Turning up Revenue
Turning up Profit
Turning up Confidence

We would require the files in a High Res format for print and a scalable transparent format for web.
(We also need greyscale and monochrome files)
All source files need to be delivered with existing layers etc

A corporate guide with the logo usage and colours should be specified.

Suggestions:
The new logo has to have CMYK colours of 100 90 0 0

CMYK 100 90 0 0
RGB #21409A
Websafe #224499
Greyscale #414141

We would also need a business card layout designed.
Could be one sided or 2 sided. Will probably print matt cello 2 sides on 350gsm gloss
Updates

Industry/Entity Type

Business

Requirements
Should not have
• Lower case n in QRV.

```html
<!DOCTYPE html>
<html lang="en">
<head>
<meta charset="utf-8">
<title>QRV Systems – Business Card</title>
<link href="https://fonts.googleapis.com/css2?family=Mulish:wght@300;400;700&display=swap" rel="stylesheet">
<style>
  :root {
    --brand-blue: #21409a;
    --canvas-grey: #dcdcdc;
    --card-white: #ffffff;
    --ink: #414141;
    --label-grey: #9a9a9a;
    --rule-grey: #b5b5b5;
    --rule-light: rgba(255,255,255,0.75);
  }
  html, body {
    margin: 0;
    padding: 0;
    overflow: hidden;
  }
  body {
    width: 1115px;
    height: 1200px;
    background: var(--canvas-grey);
    position: relative;
    font-family: "Mulish", Arial, sans-serif;
  }
  .card {
    position: absolute;
    left: 169px;
    width: 776px;
    height: 474px;
    box-shadow: 3px 4px 6px rgba(0,0,0,0.25);
    overflow: hidden;
  }
  .card--front { top: 115px; background: var(--brand-blue); color: #fff; }
  .card--back  { top: 611px; background: var(--card-white); color: var(--ink); }

  .card > * { position: absolute; margin: 0; line-height: 1; white-space: nowrap; }

  /* front */
  .wordmark { font-weight: 700; letter-spacing: 1px; }
  .card--front .wordmark { left: 29px; top: 132px; font-size: 54px; color: #fff; }
  .tagline { left: 29px; top: 305px; font-size: 32px; font-weight: 300; }
  .tagline strong { font-weight: 700; }
  .front-rule { left: 375px; top: 303px; width: 2px; height: 140px; background: var(--rule-light); }
  .address { left: 395px; top: 304px; font-size: 27px; font-weight: 300; line-height: 35px; }
  .card--front .web { left: 395px; top: 412px; font-size: 27px; font-weight: 300; }

  /* back */
  .card--back .wordmark { right: 48px; top: 55px; font-size: 38px; color: var(--brand-blue); }
  .person-name { left: 31px; top: 176px; font-size: 31px; font-weight: 300; }
  .person-role { left: 31px; top: 216px; font-size: 21px; font-weight: 400; }
  .back-rule { left: 334px; top: 176px; width: 2px; height: 204px; background: var(--rule-grey); }
  .contacts {
    left: 351px; top: 176px;
    display: grid;
    grid-template-columns: 126px auto;
    row-gap: 6px;
    font-size: 27px;
    font-weight: 400;
  }
  .contacts dt { color: var(--label-grey); font-size: 24px; font-weight: 300; line-height: 29px; }
  .contacts dd { margin: 0; line-height: 29px; }
  .email { left: 351px; top: 347px; font-size: 24px; }
  .web-band {
    left: 0; bottom: 0; width: 100%; height: 68px;
    background: var(--brand-blue);
    color: #fff;
    font-size: 25px;
    font-weight: 300;
    display: flex; align-items: center; justify-content: center;
  }
</style>
</head>
<body>
  <section class="card card--front" aria-label="Card front">
    <p class="wordmark">QRV Systems</p>
    <p class="tagline">Taking <strong>IT</strong> further</p>
    <div class="front-rule"></div>
    <p class="address">118/40 Harlow Street<br>Northmead NSW 2152</p>
    <p class="web">www.qrv.com.au</p>
  </section>

  <section class="card card--back" aria-label="Card back">
    <p class="wordmark">QRV Systems</p>
    <p class="person-name">Daniel Ashcombe</p>
    <p class="person-role">Project Director</p>
    <div class="back-rule"></div>
    <dl class="contacts">
      <dt>Phone</dt><dd>+61 2 5550 1200</dd>
      <dt>Support</dt><dd>+61 2 5550 1233</dd>
      <dt>Fax</dt><dd>+61 2 5550 1201</dd>
      <dt>Mobile</dt><dd>+61 400 555 318</dd>
    </dl>
    <p class="email">daniel.ashcombe@qrv.com.au</p>
    <p class="web-band">www.qrv.com.au</p>
  </section>
</body>
</html>
```